Collaborative Law Bus Stop Bench Design

We are looking for a design for a bus stop bench-the size is 74 inches in length and 22 inches wide.We are a group of family law lawyers, social workers and accountants who are committed to resolving marital breakdowns without going to court.
As this is a bus stop ad not a lot of words can be used.
The sign needs to show our website www.harborkinlegal.com prominently
We want the design to focus on the advantages of our process ie. not going to court-like"Don't air your dirty laundry"-a design with a clothesline or something like that.
It needs to be clear and uncomplicated but memorable.

```html
<!DOCTYPE html>
<html lang="en">
<head>
<meta charset="UTF-8">
<title>Harbor Kin Legal – Bus Stop Bench</title>
<link rel="stylesheet" href="https://fonts.googleapis.com/css2?family=Roboto:wght@300;400;700&display=swap">
<style>
  :root {
    --paper: #ffffff;
    --ink: #111111;
    --sky: #2aa3dd;
    --frame: #8fd3d3;
    --rope: #e2c23a;
    --boxers: #1f5fc8;
    --bib: #f3c6df;
    --onesie: #6e86d8;
    --bra: #c8214f;
  }
  html, body {
    margin: 0;
    padding: 0;
    overflow: hidden;
    background: var(--paper);
  }
  .bench {
    position: relative;
    width: 1200px;
    height: 357px;
    box-sizing: border-box;
    border: 2px solid var(--frame);
    background: var(--paper);
    overflow: hidden;
    font-family: "Roboto", Arial, sans-serif;
  }
  .headline {
    position: absolute;
    left: 33px;
    top: 8px;
    margin: 0;
    font-weight: 300;
    font-size: 85px;
    line-height: 81px;
    color: var(--ink);
    letter-spacing: -1px;
  }
  .headline span { display: block; }
  .headline .accent { color: var(--sky); }
  .line-art {
    position: absolute;
    left: 0;
    top: 0;
  }
  .tagline {
    position: absolute;
    left: 330px;
    top: 280px;
    width: 390px;
    margin: 0;
    text-align: center;
    color: var(--sky);
    font-weight: 700;
    font-size: 29px;
    line-height: 33px;
  }
  .web-address {
    position: absolute;
    left: 849px;
    top: 258px;
    width: 338px;
    height: 90px;
    color: var(--sky);
  }
  .web-address .prefix,
  .web-address .suffix {
    position: absolute;
    top: 0;
    font-size: 23px;
    font-weight: 400;
  }
  .web-address .prefix { left: 2px; }
  .web-address .suffix { right: 4px; }
  .web-address .name {
    position: absolute;
    left: 0;
    bottom: 0;
    width: 100%;
    height: 42px;
    background: var(--sky);
    color: var(--paper);
    font-size: 38px;
    font-weight: 400;
    line-height: 42px;
    text-align: center;
  }
</style>
</head>
<body>
  <div class="bench">
    <h1 class="headline">
      <span>Don't air</span>
      <span class="accent">your</span>
      <span>dirty</span>
      <span>laundry</span>
    </h1>

    <svg class="line-art" width="1200" height="357" viewBox="0 0 1200 357">
      <line class="clothesline" x1="335" y1="46" x2="1200" y2="42" stroke="var(--rope)" stroke-width="3"/>
      <rect class="garment-boxers" role="img" aria-label="Blue floral boxer shorts pegged on the line" x="340" y="36" width="200" height="176" rx="8" fill="var(--boxers)"/>
      <rect class="garment-bib" role="img" aria-label="Pink baby bib with teddy bear hanging from the line" x="552" y="110" width="106" height="122" rx="14" fill="var(--bib)"/>
      <rect class="garment-onesie" role="img" aria-label="Blue striped baby onesie pegged on the line" x="684" y="36" width="186" height="204" rx="12" fill="var(--onesie)"/>
      <rect class="garment-bra" role="img" aria-label="Red lace bra pegged on the line" x="868" y="36" width="298" height="150" rx="34" fill="var(--bra)"/>
    </svg>

    <p class="tagline">resolve family differences<br>without going to court</p>

    <div class="web-address">
      <span class="prefix">www.</span>
      <span class="suffix">.com</span>
      <span class="name">harborkinlegal</span>
    </div>
  </div>
</body>
</html>
```